Need home page concept design for existing website

Our existing website is www.nimbrel.com. We started re-branding project. We need one page (home page) concept made in Photoshop with a new theme. PLEASE REVIEW THE MOCK-UP OF NEW HOME PAGE IN THE ATTACHED MS DOC FILE.

We develop data processing productivity software for corporate clients. By purchasing our products and services our customers gain efficiency, cut cost, free up resources.

The new theme and styles should be modern responsive (compatible with mobile devices). Our current website's home page has lots of descriptive information which create a sense of clutter.

The new design should be clear and distinct. I like PixelHarbor.com color theme, font styles and menus. Another one I like http://velquora.com/ - the style, theme and the way they convey complicated idea to prospects.

Industry/Entity Type

Software

Font styles to use
Sans Serif

Requirements
Must have
• Clearness. Modern style. Responsive. Innovative business style that will convey new fresh approach to traditional problems our customers have. However it should not be too much extravagant, to scare off our corporate customers.

```html
<!DOCTYPE html>
<html lang="en">
<head>
<meta charset="utf-8">
<title>Nimbrel — Productivity Solutions for Trelix ERP</title>
<link href="https://fonts.googleapis.com/css2?family=Open+Sans:ital,wght@0,400;0,600;0,700;1,400&family=Ubuntu:wght@500;700&family=Oswald:wght@400;500&display=swap" rel="stylesheet">
<style>
:root{
  --blue:#1a78b8;
  --blue-dark:#0f5e98;
  --blue-light:#3fa3dd;
  --orange:#f4741e;
  --orange-light:#ff9440;
  --text:#555;
  --text-dark:#333;
  --grey:#8a8a8a;
  --line:#d9d9d9;
  --page:#f8f9f9;
}
*{box-sizing:border-box;margin:0;padding:0}
html,body{width:1024px;height:1200px;overflow:hidden}
body{position:relative;background:var(--page);font-family:'Open Sans',sans-serif;color:var(--text)}
.abs{position:absolute}

/* header */
.site-header{position:absolute;left:0;top:0;width:1024px;height:77px;background:#fff}
.brand{left:134px;top:14px;font-family:'Ubuntu',sans-serif;font-weight:700;font-size:34px;color:var(--blue);letter-spacing:1px}
.brand-divider{left:311px;top:13px;width:1px;height:44px;background:#e2e2e2}
.tagline{left:326px;top:17px;font-style:italic;font-size:13px;line-height:19px;color:var(--grey)}
.btn{display:flex;align-items:center;justify-content:center;color:#fff;font-family:'Oswald',sans-serif;font-size:12.5px;letter-spacing:.3px;border-radius:2px}
.btn-quote{left:649px;top:18px;width:111px;height:35px;background:linear-gradient(#3d9ad6,#1c74b4);border:1px solid #1766a0}
.btn-trial{left:776px;top:18px;width:112px;height:35px;background:linear-gradient(#ff8a34,#f0620f);border:1px solid #d9560c}

/* nav */
.main-nav{left:0;top:77px;width:1024px;height:41px;background:linear-gradient(#3a9bd6,#1b73b3);border-top:2px solid #5cb3e6}
.main-nav ul{list-style:none}
.main-nav li{position:absolute;top:10px;color:#fff;font-family:'Oswald',sans-serif;font-size:14px;letter-spacing:.2px}
.search{left:711px;top:7px;width:176px;height:24px;background:#fff;border:1px solid #cfd8de;font-size:10px;color:#777;padding:5px 6px}
.search svg{position:absolute;right:6px;top:5px}

/* hero */
.hero{left:0;top:118px;width:1024px;height:300px;background:linear-gradient(90deg,#e7eaee 0%,#eef0f1 40%,#e6e0da 70%,#d9cdc2 100%)}
.hero-photo{left:640px;top:0;width:384px;height:300px;background:linear-gradient(100deg,rgba(236,233,229,0) 0%,#d8c6b6 25%,#c9a488 55%,#e9e6e4 80%,#cfcfd2 100%)}
.hero h1{left:134px;top:54px;width:540px;font-family:'Ubuntu',sans-serif;font-weight:500;font-size:27px;line-height:36px;color:var(--blue)}
.hero p{left:137px;top:147px;width:500px;font-size:13.5px;line-height:20px;color:#555}
.hero b{color:#444}

/* video + signup */
.video{left:134px;top:457px;width:360px;height:215px;background:linear-gradient(135deg,#7a93ad,#aab8c7 45%,#c9ced4 70%,#8ea0b4)}
.video-title{left:0;top:70px;width:360px;text-align:center;font-family:'Ubuntu',sans-serif;font-weight:700;font-size:44px;letter-spacing:-1.5px;color:var(--blue-dark)}
.video-sub{left:118px;top:118px;font-style:italic;font-size:13px;color:#222}
.video-bar{left:0;top:200px;width:360px;height:15px;background:#1b1b1b;font-size:5px;color:#ddd;padding:5px 0 0 38px}
.video-bar i{position:absolute;left:0;top:0;width:90px;height:2px;background:#d22}
.signup{left:518px;top:458px;width:369px;height:80px;background:#f1f1f1;border:1px solid #dcdcdc}
.signup h3{left:25px;top:10px;font-size:13.5px;font-weight:600;color:var(--text-dark)}
.signup h3 span{color:var(--orange)}
.signup .email{left:22px;top:34px;width:236px;height:32px;background:#fff;border:1px solid #d2d2d2;font-size:10px;color:#888;padding:9px 12px}
.signup .submit{left:257px;top:34px;width:88px;height:32px;background:linear-gradient(#4db0ea,#2891d6);border:1px solid #1f7fc0;color:#fff;font-size:12px;font-weight:600;display:flex;align-items:center;justify-content:center}
.intro{left:520px;top:552px;width:370px;font-size:13.5px;line-height:20px;color:#555}
.intro p+p{margin-top:16px}

/* modules */
.modules-title{left:135px;top:716px;font-family:'Ubuntu',sans-serif;font-weight:500;font-size:20px;color:var(--blue)}
.module{left:137px;width:400px;height:62px}
.module .icon{position:absolute;left:0;top:0;width:62px;height:62px;border-radius:50%;background:radial-gradient(circle at 40% 35%,#fff,#e8e8e8);box-shadow:0 2px 4px rgba(0,0,0,.18);display:flex;align-items:center;justify-content:center}
.module span{position:absolute;left:76px;top:16px;font-size:20.5px;color:#555}

/* events */
.events-title{left:533px;top:716px;font-family:'Ubuntu',sans-serif;font-weight:500;font-size:20.5px;color:var(--blue);padding-left:24px}
.events-title svg{position:absolute;left:0;top:5px}
.event{left:533px;width:356px;height:160px}
.event h4{font-size:13px;font-weight:700;color:#333}
.event h4 span{color:#777;font-weight:600}
.event p{margin-top:8px;font-size:13.5px;line-height:19px;color:#8a8a8a}
.event .date{position:absolute;left:0;top:103px;font-size:10px;color:#666;padding-left:14px}
.event .date svg{position:absolute;left:0;top:2px}
.event .register{position:absolute;left:266px;top:87px;width:88px;height:31px;background:linear-gradient(#ff8a34,#f0620f);border:1px solid #dc5a10;color:#fff;font-size:12px;font-weight:600;display:flex;align-items:center;justify-content:center}
.event .rule{position:absolute;left:-1px;top:126px;width:358px;height:1px;background:var(--line)}
.event-links{left:535px;top:1088px;font-size:13px;font-weight:600;color:#999;letter-spacing:.3px}
.event-links a{color:#999;text-decoration:underline}
.event-links .sep{margin:0 30px;color:#ccc}

/* footer */
.site-footer{left:0;top:1143px;width:1024px;height:57px;background:linear-gradient(#2d8fd0,#1562a5);border-top:2px solid #58b0e6}
.copyright{left:133px;top:21px;font-size:10px;color:#0d3f6c}
.social{left:733px;top:17px;display:flex;gap:4px}
.social i{display:block;width:22px;height:22px;border-radius:50%;border:2px solid #0d3f6c}
</style>
</head>
<body>

<header class="site-header">
  <div class="abs brand">Nimbrel</div>
  <div class="abs brand-divider"></div>
  <div class="abs tagline">Easy Productivity Solutions for<br>Managing Your Trelix ERP Data</div>
  <a class="abs btn btn-quote">REQUEST A QUOTE</a>
  <a class="abs btn btn-trial">GET A FREE TRIAL</a>
</header>

<nav class="abs main-nav">
  <ul>
    <li style="left:137px">HOME</li>
    <li style="left:196px">DATA LOADERS</li>
    <li style="left:300px">WEB SOLUTIONS</li>
    <li style="left:413px">OUTPUT SOLUTIONS</li>
    <li style="left:544px">ABOUT</li>
    <li style="left:607px">CONTACT</li>
  </ul>
  <div class="abs search">Search
    <svg width="12" height="12" viewBox="0 0 12 12"><circle cx="5" cy="5" r="3.8" fill="none" stroke="#666" stroke-width="1.6"/><line x1="7.8" y1="7.8" x2="11" y2="11" stroke="#666" stroke-width="1.8"/></svg>
  </div>
</nav>

<section class="abs hero">
  <div class="abs hero-photo" role="img" aria-label="Photo of a smiling woman using a tablet"></div>
  <h1 class="abs">Quickly &amp; Safely Manage Complex Trelix Tasks and Significantly Increase Efficiency</h1>
  <p class="abs">Your company needs to be nimble. Your customers demand it. Your competition challenges it. Your survival depends on it. Don’t get bogged down by cumbersome Trelix ERP tasks when <b>Nimbrel’s easy-to-use, safe and simple</b> solutions can <b>triple</b> your productivity.</p>
</section>

<div class="abs video" role="img" aria-label="Video thumbnail: office team working at a laptop">
  <div class="abs video-title">DATA LOADER</div>
  <div class="abs video-sub">Productivity Solutions for Trelix ERP</div>
  <div class="abs video-bar"><i></i>0:02 / 4:17</div>
</div>

<form class="abs signup">
  <h3 class="abs"><span>Sign up</span> to learn about fascinating solutions</h3>
  <div class="abs email">Enter Your Email Address</div>
  <div class="abs submit">Submit</div>
</form>

<div class="abs intro">
  <p>Find out more about what makes Data Loaders the perfect solution for Trelix data management!</p>
  <p>Download your Trelix ERP data into easy-to-use Gridly spread-sheets where you can make massive changes and upload them safely to back Trelix.</p>
</div>

<h2 class="abs modules-title">Browse our DATA LOADER modules:</h2>

<div class="abs module" style="top:760px">
  <div class="icon"><svg width="26" height="22" viewBox="0 0 26 22" fill="none" stroke="#1a78b8" stroke-width="1.8"><rect x="2" y="4" width="22" height="13"/><line x1="7" y1="14" x2="7" y2="10"/><line x1="11" y1="14" x2="11" y2="7"/><line x1="15" y1="14" x2="15" y2="9"/><line x1="19" y1="14" x2="19" y2="6"/><line x1="8" y1="20" x2="18" y2="20"/></svg></div>
  <span>Master Data &amp; Inventory</span>
</div>
<div class="abs module" style="top:841px">
  <div class="icon"><svg width="28" height="24" viewBox="0 0 28 24" fill="none" stroke="#1a78b8" stroke-width="1.8"><circle cx="7" cy="12" r="5"/><line x1="12" y1="12" x2="16" y2="12"/><polyline points="16,4 16,20"/><rect x="18" y="2" width="7" height="5"/><rect x="18" y="9.5" width="7" height="5"/><rect x="18" y="17" width="7" height="5"/></svg></div>
  <span>Distribution &amp; Supply Chain</span>
</div>
<div class="abs module" style="top:922px">
  <div class="icon"><svg width="26" height="26" viewBox="0 0 26 26" fill="none" stroke="#1a78b8" stroke-width="2"><path d="M21 8a10 10 0 1 0 1 8"/><polyline points="22,3 22,8 17,8"/><text x="13" y="17.5" font-size="11" font-family="Open Sans,sans-serif" font-weight="700" fill="#1a78b8" stroke="none" text-anchor="middle">$</text></svg></div>
  <span>Finance</span>
</div>
<div class="abs module" style="top:999px">
  <div class="icon"><svg width="28" height="24" viewBox="0 0 28 24" fill="none" stroke="#1a78b8" stroke-width="1.8"><circle cx="4" cy="18" r="2.5"/><circle cx="12" cy="13" r="2.5"/><circle cx="17" cy="18" r="2.5"/><circle cx="24" cy="5" r="3"/><polyline points="6,17 10,14 15,17 22,7"/></svg></div>
  <span>Production</span>
</div>

<h2 class="abs events-title"><svg width="16" height="16" viewBox="0 0 16 16" fill="none" stroke="#666" stroke-width="1.5"><rect x="1" y="3" width="14" height="12"/><line x1="1" y1="6.5" x2="15" y2="6.5"/><line x1="4.5" y1="1" x2="4.5" y2="4"/><line x1="11.5" y1="1" x2="11.5" y2="4"/></svg>Upcoming Events</h2>

<article class="abs event" style="top:763px">
  <h4><span>WEBINARS:</span> Transforming Your Fiscal EOY Process</h4>
  <p>The point of using Lorem Ipsum is that it has a more-or-less normal distribution of letters, as opposed to using 'Content here, content here'.</p>
  <div class="date"><svg width="9" height="9" viewBox="0 0 9 9" fill="none" stroke="#999"><rect x=".5" y="1.5" width="8" height="7"/><line x1=".5" y1="3.5" x2="8.5" y2="3.5"/></svg>8 December 2013</div>
  <a class="register">Register</a>
  <div class="rule"></div>
</article>
<article class="abs event" style="top:923px">
  <h4><span>WEBINARS:</span> Transforming Your Fiscal EOY Process</h4>
  <p>The point of using Lorem Ipsum is that it has a more-or-less normal distribution of letters, as opposed to using 'Content here, content here'.</p>
  <div class="date"><svg width="9" height="9" viewBox="0 0 9 9" fill="none" stroke="#999"><rect x=".5" y="1.5" width="8" height="7"/><line x1=".5" y1="3.5" x2="8.5" y2="3.5"/></svg>8 December 2013</div>
  <a class="register">Register</a>
  <div class="rule"></div>
</article>

<div class="abs event-links"><a>VIEW PAST WEBINARS</a><span class="sep">|</span><a>REQUEST A WEBINAR</a></div>

<footer class="abs site-footer">
  <div class="abs copyright">Copyright © 2014 Nimbrel. All Rights Reserved. Privacy Policy | &nbsp;Contact Us</div>
  <div class="abs social" aria-label="Social links"><i></i><i></i><i></i><i></i><i></i><i></i></div>
</footer>

</body>
</html>
```